Irrigation label

This will be a card attached to a flyer concerning irrigation service that asks the customer to stick the card to their sprinkler control box and each time we see the card they will get 10% off their billing

Industry/Entity Type

It Service

Contact Information for Business Card

Hadley Lawn Service Logo Irrigation Service
Owen Pettigrew LI: 0047261
10% off on Parts and Labor 979 555-0184

```html
<!DOCTYPE html>
<html lang="en">
<head>
<meta charset="utf-8">
<title>Hadley Lawn Service – Irrigation Card</title>
<link rel="stylesheet" href="https://fonts.googleapis.com/css2?family=Open+Sans:wght@400;600;700&display=swap">
<style>
  :root {
    --canvas-bg: #ececec;
    --card-bg: #ffffff;
    --field-green: #0f5129;
    --accent-green: #7bd14a;
    --text-light: #ffffff;
    --card-shadow: rgba(0, 0, 0, 0.18);
  }
  * { margin: 0; padding: 0; box-sizing: border-box; }
  html, body {
    width: 1200px;
    height: 800px;
    overflow: hidden;
    background: var(--canvas-bg);
    font-family: "Open Sans", Arial, sans-serif;
  }
  .canvas {
    position: relative;
    width: 1200px;
    height: 800px;
    display: flex;
    align-items: center;
    justify-content: center;
  }
  .card {
    position: relative;
    width: 840px;
    height: 480px;
    background: var(--card-bg);
    box-shadow: 0 10px 30px var(--card-shadow);
    overflow: hidden;
  }
  .card__field {
    position: absolute;
    inset: 0;
    width: 100%;
    height: 100%;
  }
  .contact-name {
    position: absolute;
    left: 300px;
    top: 70px;
    color: var(--text-light);
    font-weight: 700;
    font-size: 24px;
    line-height: 1.1;
  }
  .contact-role {
    position: absolute;
    left: 300px;
    top: 100px;
    color: var(--accent-green);
    font-weight: 400;
    font-size: 17px;
  }
  .brand-name {
    position: absolute;
    left: 0;
    right: 0;
    top: 160px;
    text-align: center;
    color: var(--text-light);
    font-weight: 600;
    font-size: 50px;
    line-height: 1.05;
  }
  .detail-row {
    position: absolute;
    display: flex;
    align-items: center;
    gap: 12px;
    color: var(--text-light);
    font-size: 19px;
  }
  .detail-row--licence { left: 190px; top: 318px; }
  .detail-row--phone { left: 440px; top: 318px; }
  .detail-icon { width: 40px; height: 40px; flex: none; }
  .offer {
    position: absolute;
    left: 190px;
    top: 378px;
    color: var(--text-light);
    font-size: 25px;
  }
</style>
</head>
<body>
<main class="canvas">
  <article class="card" aria-label="Hadley Lawn Service irrigation discount card">
    <svg class="card__field" viewBox="0 0 840 480" aria-hidden="true">
      <ellipse cx="420" cy="240" rx="405" ry="232" fill="var(--field-green)"/>
    </svg>

    <p class="contact-name">Owen Pettigrew</p>
    <p class="contact-role">Irrigation Service</p>

    <h1 class="brand-name">Hadley<br>Lawn Service</h1>

    <div class="detail-row detail-row--licence">
      <svg class="detail-icon" viewBox="0 0 40 40" aria-hidden="true">
        <ellipse cx="20" cy="20" rx="18" ry="15" fill="none" stroke="var(--text-light)" stroke-width="2"/>
        <rect x="16" y="9" width="8" height="10" rx="4" fill="none" stroke="var(--text-light)" stroke-width="2"/>
        <rect x="16" y="21" width="8" height="10" rx="4" fill="none" stroke="var(--text-light)" stroke-width="2"/>
      </svg>
      <span>LI: 0047261</span>
    </div>

    <div class="detail-row detail-row--phone">
      <svg class="detail-icon" viewBox="0 0 40 40" aria-hidden="true">
        <ellipse cx="20" cy="20" rx="18" ry="15" fill="none" stroke="var(--text-light)" stroke-width="2"/>
        <rect x="14" y="8" width="12" height="24" rx="2" fill="none" stroke="var(--text-light)" stroke-width="2"/>
        <line x1="18" y1="28" x2="22" y2="28" stroke="var(--text-light)" stroke-width="2"/>
      </svg>
      <span>979 555-0184</span>
    </div>

    <p class="offer">10% off on Parts and Labor</p>
  </article>
</main>
</body>
</html>
```